Biz Card & Stationary: Modern, boutique appeal for vacation rental company for high end luxury homes
Biz Card + Folder + Letterhead + Envelope
Simple
Marla Whitcombe
Owner
2817 Maple Hollow Ln Larkspur TX 78529
marla@quolbi.com
www.quolbi.com
-may create image or graphic to use with logo -Need letterhead & envelopes in word format

```html
<!DOCTYPE html>
<html lang="en">
<head>
<meta charset="utf-8">
<title>Quolbi Vacation Rentals – Stationery</title>
<link rel="stylesheet" href="https://fonts.googleapis.com/css2?family=Raleway:wght@300;400;500&family=Arimo:wght@400&display=swap">
<style>
  :root {
    --bg: #e4e6e7;
    --paper: #ffffff;
    --teal: #4fb3bd;
    --teal-dark: #3a9aa4;
    --ink: #4a4f52;
    --soft-ink: #8a9094;
    --shadow: rgba(0,0,0,0.14);
  }
  * { box-sizing: border-box; margin: 0; padding: 0; }
  html, body { width: 1200px; height: 961px; overflow: hidden; }
  body {
    position: relative;
    background: var(--bg);
    font-family: "Arimo", Arial, sans-serif;
    color: var(--ink);
  }
  .sheet {
    position: absolute;
    background: var(--paper);
    box-shadow: 0 3px 10px var(--shadow);
  }
  .brand { font-family: "Raleway", sans-serif; color: var(--teal); }
  .brand-name { font-weight: 300; letter-spacing: 1px; line-height: 1; }
  .brand-tag { font-weight: 300; letter-spacing: 3px; text-transform: uppercase; }

  /* Letterhead */
  .letterhead { left: 70px; top: 50px; width: 530px; height: 686px; border-bottom: 6px solid var(--teal); }
  .letterhead .brand { position: absolute; left: 270px; top: 34px; }
  .letterhead .brand-name { font-size: 40px; }
  .letterhead .brand-tag { font-size: 8px; margin-top: 3px; }
  .letter { position: absolute; left: 60px; top: 150px; width: 400px; font-size: 9.5px; line-height: 1.55; }
  .letter .recipient { margin-bottom: 16px; }
  .letter p { margin-bottom: 12px; }
  .signature { width: 120px; height: 34px; background: linear-gradient(90deg, #d9dcde, #eceeef); margin: 4px 0 6px; }
  .signer { font-size: 9.5px; }
  .letter-footer { position: absolute; left: 60px; bottom: 22px; font-family: "Raleway", sans-serif; font-size: 8.5px; color: var(--teal-dark); line-height: 1.6; }
  .letter-footer .rule { width: 230px; height: 1px; background: var(--teal); margin-bottom: 5px; }

  /* Business cards */
  .card { width: 320px; height: 183px; }
  .card-front { left: 700px; top: 90px; }
  .card-front .brand { position: absolute; left: 150px; top: 22px; }
  .card-front .brand-name { font-size: 34px; }
  .card-front .brand-tag { font-size: 7px; margin-top: 2px; }
  .card-front .person { position: absolute; left: 150px; top: 90px; font-size: 10px; line-height: 1.5; }
  .card-front .person strong { font-weight: 400; color: var(--teal-dark); }
  .card-front .contact { position: absolute; left: 20px; bottom: 16px; font-family: "Raleway", sans-serif; font-size: 8px; color: var(--teal-dark); line-height: 1.5; }
  .card-front .edge { position: absolute; left: 0; right: 0; bottom: 0; height: 5px; background: var(--teal); }

  .card-back { left: 700px; top: 300px; background: var(--teal); display: flex; align-items: center; justify-content: center; }
  .card-back .brand { color: var(--paper); text-align: left; }
  .card-back .brand-name { font-size: 52px; }
  .card-back .brand-tag { font-size: 9px; margin-top: 3px; }

  /* Envelope */
  .envelope { left: 630px; top: 540px; width: 500px; height: 220px; border-bottom: 5px solid var(--teal); }
  .envelope .brand { position: absolute; left: 26px; top: 20px; }
  .envelope .brand-name { font-size: 36px; }
  .envelope .brand-tag { font-size: 7.5px; margin-top: 2px; }
  .envelope .return { position: absolute; left: 26px; bottom: 16px; font-family: "Raleway", sans-serif; font-size: 8.5px; color: var(--teal-dark); }
  .envelope .return .rule { width: 220px; height: 1px; background: var(--teal); margin-bottom: 5px; }
  .envelope .web { position: absolute; right: 26px; bottom: 16px; font-family: "Raleway", sans-serif; font-size: 8.5px; color: var(--teal-dark); }
</style>
</head>
<body>

  <section class="sheet letterhead" aria-label="Letterhead">
    <div class="brand">
      <div class="brand-name">Quolbi</div>
      <div class="brand-tag">Vacation Rentals</div>
    </div>
    <div class="letter">
      <div class="recipient">Ms. Renata Delgado<br>Guest Services Manager<br>Hilltop Suites<br>420 Cedar Bluff Dr<br>Millbrook, TX 78633</div>
      <p>Dear Ms. Delgado:</p>
      <p>I am excited to share our new season of private retreats with you. Each home in our collection has been selected for comfort, privacy and style.</p>
      <p>Our team handles every detail, from arrival to departure, so that your guests can simply relax. We offer concierge planning, daily housekeeping and local dining guides.</p>
      <p>I would welcome the chance to walk you through our newest properties. Please reach out at your convenience.</p>
      <p>Warm regards,</p>
      <div class="signature" role="img" aria-label="Handwritten signature"></div>
      <div class="signer">Marla Whitcombe<br>Owner</div>
    </div>
    <div class="letter-footer">
      <div class="rule"></div>
      2817 Maple Hollow Ln, Larkspur, TX 78529<br>
      Cell 555.010.0148 &nbsp;|&nbsp; marla@quolbi.com &nbsp;|&nbsp; www.quolbi.com
    </div>
  </section>

  <section class="sheet card card-front" aria-label="Business card front">
    <div class="brand">
      <div class="brand-name">Quolbi</div>
      <div class="brand-tag">Vacation Rentals</div>
    </div>
    <div class="person"><strong>Marla Whitcombe</strong><br>Owner</div>
    <div class="contact">2817 Maple Hollow Ln, Larkspur, TX 78529<br>marla@quolbi.com &nbsp;|&nbsp; www.quolbi.com</div>
    <div class="edge"></div>
  </section>

  <section class="sheet card card-back" aria-label="Business card back">
    <div class="brand">
      <div class="brand-name">Quolbi</div>
      <div class="brand-tag">Vacation Rentals</div>
    </div>
  </section>

  <section class="sheet envelope" aria-label="Envelope">
    <div class="brand">
      <div class="brand-name">Quolbi</div>
      <div class="brand-tag">Vacation Rentals</div>
    </div>
    <div class="return">
      <div class="rule"></div>
      2817 Maple Hollow Ln, Larkspur, TX 78529
    </div>
    <div class="web">www.quolbi.com</div>
  </section>

</body>
</html>
```